Creation of a Velmora Flyer design

As part of the cr% 26 # 233; ation of our soci% 26 # 233; t% 26 # 233 ;, we wish to cr% 26 # 233; er a flyer pr% 26 # 233; feeling our diff% 26 # 233; annuities% 26 # 233; s business advisory services% 26 # 233; foreign% 26 # 232; res who wish to develop their activities% 26 # 233; s in Switzerland. We want a double-sided flyer that presents% 26 # 233; society% 26 # 233; t% 26 # 233; d% 26 # 39; a c% 26 # 244; t% 26 # 233; and who presents% 26 # 233; benefits of the other. We have d% 26 # 233; j% 26 # 224; made a very basic provisional flyer to be able to present our activities. We put it to you as an example.

Target Market(s)

European companies% 26 # 233; internal% 26 # 233; res% 26 # 233; es by the market% 26 # 233; Swiss

Industry/Entity Type

Business Consultant

Colors

Designer to choose colors to be used in the design.

Requirements
Must have
• Company name and contact details
A field to detail the services
Nice to have
• Some% 26 # 233; l% 26 # 233; elements that recall Switzerland and some% 26 # 233; l% 26 # 233; elements that recall c% 26 # 244; t% 26 # 233; % 26quot; business% 26quot;

```html
<!DOCTYPE html>
<html lang="en">
<head>
<meta charset="utf-8">
<title>Velmora Flyer</title>
<link href="https://fonts.googleapis.com/css2?family=Raleway:wght@300;400;500;700&display=swap" rel="stylesheet">
<style>
  :root {
    --teal: #1d8ab0;
    --ink: #1f2b36;
    --white: #ffffff;
    --backdrop: #d9d9d6;
  }
  * { margin: 0; padding: 0; box-sizing: border-box; }
  html, body { width: 1200px; height: 902px; overflow: hidden; }
  body { background: var(--backdrop); font-family: "Raleway", sans-serif; position: relative; }
  .line { display: block; white-space: nowrap; }
  .page {
    position: absolute; top: 47px; width: 556px; height: 788px;
    background: var(--white); overflow: hidden;
    box-shadow: 0 2px 8px rgba(0,0,0,.18);
  }
  .page--front { left: 30px; }
  .page--back { left: 610px; }

  /* Front */
  .hero-photo {
    position: absolute; left: 0; top: 0; width: 556px; height: 290px;
    background: linear-gradient(160deg, #cfe0ea 0%, #8fb3c9 30%, #4d86a8 55%, #1f5a80 80%, #163f5d 100%);
  }
  .hero-title {
    position: absolute; right: 46px; top: 56px; text-align: right;
    color: var(--white); font-weight: 300; font-size: 26px; line-height: 28px;
  }
  .teal-panel { position: absolute; left: 240px; top: 279px; width: 316px; height: 509px; background: var(--teal); }
  .lake-photo {
    position: absolute; left: 0; top: 265px; width: 334px; height: 149px;
    background: linear-gradient(180deg, #9fc7e0 0%, #6f9f6a 38%, #b7a48a 55%, #2fa8b4 72%, #1f8a9e 100%);
    clip-path: polygon(0 0, 100% 0, 83% 100%, 0 100%);
  }
  .intro { position: absolute; left: 300px; top: 315px; color: var(--white); font-size: 11.2px; line-height: 17.8px; }
  .intro .line:nth-child(1) { padding-left: 31px; }
  .intro .line:nth-child(2) { padding-left: 23px; }
  .intro .line:nth-child(3) { padding-left: 15px; }
  .intro .line:nth-child(4) { padding-left: 7px; }
  .panel-copy { position: absolute; left: 280px; top: 429px; color: var(--white); font-size: 11.2px; line-height: 17.8px; }
  .panel-copy p + p { margin-top: 24px; }
  .footnote { font-size: 5px; margin-left: 12px; }
  .lead-copy { position: absolute; left: 48px; top: 443px; color: var(--teal); font-size: 14px; line-height: 21.1px; }
  .brand { position: absolute; display: flex; align-items: center; }
  .brand__mark { display: block; border-radius: 6px; }
  .brand__name { font-weight: 300; letter-spacing: 2.5px; line-height: 1; }
  .brand--front { left: 277px; top: 707px; gap: 19px; }
  .brand--front .brand__mark { background: var(--white); width: 36px; height: 36px; }
  .brand--front .brand__name { color: var(--white); font-size: 32px; }

  /* Back */
  .side-band { position: absolute; left: 0; top: 0; width: 52px; height: 788px; background: var(--teal); }
  .back-title {
    position: absolute; left: 91px; top: 47px; color: var(--ink);
    font-weight: 300; font-size: 23.5px; line-height: 25.3px;
  }
  .bridge-photo {
    position: absolute; left: 0; top: 175px; width: 302px; height: 152px;
    background: linear-gradient(180deg, #a9c9e3 0%, #7da7c9 35%, #9b5a32 52%, #c0392b 62%, #6a4a2e 75%, #3d7da3 100%);
    clip-path: polygon(0 0, 100% 0, 81% 100%, 0 100%);
  }
  .offer { position: absolute; left: 266px; top: 174px; color: var(--teal); font-size: 13.6px; line-height: 19.7px; }
  .offer .line:nth-child(1) { padding-left: 50px; }
  .offer .line:nth-child(2) { padding-left: 42px; }
  .offer .line:nth-child(3) { padding-left: 34px; }
  .offer .line:nth-child(4) { padding-left: 30px; }
  .offer .line:nth-child(5) { padding-left: 22px; }
  .offer .line:nth-child(6) { padding-left: 14px; }
  .offer .line:nth-child(7) { padding-left: 5px; }
  .services {
    position: absolute; left: 98px; top: 350px; list-style: none;
    color: var(--ink); font-size: 10.8px; line-height: 16.8px;
  }
  .services li { position: relative; padding-left: 7px; margin-bottom: 7.7px; }
  .services li::before { content: "•"; position: absolute; left: 0; }
  .contact-call { position: absolute; left: 105px; top: 654px; color: var(--ink); font-weight: 700; font-size: 11px; line-height: 16px; }
  .brand--back { right: 50px; top: 669px; gap: 18px; }
  .brand--back .brand__mark { background: var(--ink); width: 31px; height: 31px; }
  .brand--back .brand__name { color: var(--ink); font-size: 30px; }
  .contact {
    position: absolute; right: 51px; top: 705px; text-align: right; font-style: normal;
    color: var(--ink); font-size: 10.8px; line-height: 16.8px;
  }
  .contact strong { font-weight: 700; }
</style>
</head>
<body>

<section class="page page--front">
  <div class="hero-photo" role="img" aria-label="Snow-capped Alpine peak above green valleys under a blue sky"></div>
  <h1 class="hero-title">Velmora is there<br>to support you in<br>your administrative<br>and strategic<br>procedures!</h1>
  <div class="teal-panel"></div>
  <div class="lake-photo" role="img" aria-label="Lakeside castle with turrets on turquoise water, mountains behind"></div>
  <p class="intro">
    <span class="line">Velmora strives to deepen the</span>
    <span class="line">understanding of your business and</span>
    <span class="line">acts as your local partner. We assist you</span>
    <span class="line">in defining together all the services that</span>
    <span class="line">best meet your needs.</span>
  </p>
  <div class="panel-copy">
    <p>
      <span class="line">Our consulting skills are focused on high added</span>
      <span class="line">value sectors, such as food and beverages,</span>
      <span class="line">fashion and lifestyle, products and services for</span>
      <span class="line">leading industries (pharmaceutical, chemical,</span>
      <span class="line">precision mechanics) or sustainable solutions</span>
      <span class="line">(renewable energies, recyclable materials).</span>
    </p>
    <p>
      <span class="line">From our office in Neuchâtel* and with our</span>
      <span class="line">language knowledges, we are able to cover the</span>
      <span class="line">whole of Switzerland. Having many years of</span>
      <span class="line">experience in economic promotion and business</span>
      <span class="line">management, we are familiar with the Swiss</span>
      <span class="line">trade and foreign companies wishing to export</span>
      <span class="line">to Switzerland.<span class="footnote">* as of August 2020, we will open an office in Zurich as</span></span>
    </p>
  </div>
  <p class="lead-copy">
    <span class="line">The potential of the Swiss</span>
    <span class="line">market offers many</span>
    <span class="line">business opportunities</span>
    <span class="line">to foreign companies,</span>
    <span class="line">however there are some</span>
    <span class="line">tariff and non-tariff</span>
    <span class="line">barriers to cope with,</span>
    <span class="line">such as its strong</span>
    <span class="line">requirements in terms of</span>
    <span class="line">quality and innovation,</span>
    <span class="line">cultural and linguistic</span>
    <span class="line">differences, specific rules</span>
    <span class="line">applied to certain</span>
    <span class="line">products or services.</span>
  </p>
  <div class="brand brand--front">
    <span class="brand__mark"></span>
    <span class="brand__name">VELMORA</span>
  </div>
</section>

<section class="page page--back">
  <div class="side-band"></div>
  <h2 class="back-title">
    <span class="line">You are convinced of the potential of</span>
    <span class="line">your product or service and you wish</span>
    <span class="line">to focus on the Swiss market, or you</span>
    <span class="line">want to expand your market share!</span>
  </h2>
  <div class="bridge-photo" role="img" aria-label="Covered wooden bridge with red flower boxes and a stone water tower on a lake"></div>
  <p class="offer">
    <span class="line">Thanks to its personalized</span>
    <span class="line">approach and tailor-made</span>
    <span class="line">assistance, Velmora offers you</span>
    <span class="line">the right support to develop your</span>
    <span class="line">business activities and answers to</span>
    <span class="line">all your questions about the Swiss</span>
    <span class="line">market. As a partner we assist you</span>
    <span class="line">in finding market opportunities:</span>
  </p>
  <ul class="services">
    <li><span class="line">By providing commercial contacts that match your target profiles;</span></li>
    <li><span class="line">By listing the legal and regulatory requirements specific to the Swiss</span><span class="line">market (Switzerland is not an EU member State);</span></li>
    <li><span class="line">By putting you in contact with private or public interlocutors in the</span><span class="line">context of an individual contact programme;</span></li>
    <li><span class="line">By preparing a market study that measures the potential of your</span><span class="line">product or service;</span></li>
    <li><span class="line">By adapting your marketing material (website, brochures, flyers, etc.)</span><span class="line">to the specific needs of the Swiss market and by translating it into</span><span class="line">German and/or French;</span></li>
    <li><span class="line">By organizing a promotional event that is tailored to your needs;</span></li>
    <li><span class="line">By representing you at trade shows or fairs;</span></li>
    <li><span class="line">By assuming the fiscal representation of your company;</span></li>
    <li><span class="line">By offering you logistical and administrative support.</span></li>
  </ul>
  <p class="contact-call">Contact us!</p>
  <div class="brand brand--back">
    <span class="brand__mark"></span>
    <span class="brand__name">VELMORA</span>
  </div>
  <address class="contact">
    <strong>Neuchâtel Office</strong> Velmora Sàrl<br>
    Rue des Vergers 7 | 2015 Areuse (Neuchâtel) +41 (0)32 555 01 23<br>
    info@velmora.ch | www.velmora.ch
  </address>
</section>

</body>
</html>
```